Business Cards

The name of our firm is "Bayfield Insurance adjusters"
We separate ourselves from all other public adjusters because most of us worked for the insurance companies so we understand their games.
As Insurance adjusters we represent the Insured, not the insurance companies. Our # 1 priority is to handle the entire claim process as seamless as possible on behalf of the homeowner/business owner so they don't have to deal with the hassles and headaches. Just as the logo your team designed, I want the cards to stand out from everyone elses. I also want the cards to help better understand our services and Value on hiring us and value that we can offer.
I uploaded the logo whenever I created the project. I don't see an option on re uploading the logo anywhere. Any advise??

```html
<!DOCTYPE html>
<html lang="en">
<head>
<meta charset="utf-8">
<title>Bayfield Insurance Adjusters – Business Cards</title>
<link href="https://fonts.googleapis.com/css2?family=Jost:wght@400;500;600&display=swap" rel="stylesheet">
<style>
  :root {
    --backdrop: #262626;
    --card-front: #0f0f10;
    --card-back: #131314;
    --pattern-tone: #1c1c1e;
    --brand-blue: #0a7fb8;
    --ink-light: #f2f2f2;
    --card-shadow: rgba(0, 0, 0, 0.55);
  }
  * { margin: 0; padding: 0; box-sizing: border-box; }
  html, body {
    width: 1200px;
    height: 1108px;
    overflow: hidden;
    background: var(--backdrop);
    font-family: "Jost", "Futura", sans-serif;
  }
  .canvas {
    position: relative;
    width: 1200px;
    height: 1108px;
  }
  .card {
    position: absolute;
    top: 224px;
    width: 380px;
    height: 660px;
    border-radius: 22px;
    overflow: hidden;
    box-shadow: 0 18px 40px var(--card-shadow);
  }
  .card--front {
    left: 170px;
    background: var(--card-front);
  }
  .card--back {
    left: 650px;
    background: var(--card-back);
  }

  /* Front side */
  .contact {
    position: absolute;
    top: 72px;
    left: 0;
    right: 0;
    text-align: center;
  }
  .contact__name {
    font-weight: 600;
    font-size: 30px;
    letter-spacing: 0.5px;
    color: var(--brand-blue);
    text-transform: uppercase;
  }
  .contact__lines {
    margin-top: 22px;
    list-style: none;
    font-weight: 400;
    font-size: 19px;
    line-height: 1.35;
    color: var(--ink-light);
  }
  .contact__highlight { color: var(--brand-blue); }

  .front-mark {
    position: absolute;
    left: 30px;
    right: 24px;
    bottom: 52px;
    font-weight: 600;
    color: var(--brand-blue);
    text-transform: uppercase;
  }
  .front-mark__name {
    font-size: 122px;
    line-height: 0.92;
    letter-spacing: 1px;
  }
  .front-mark__tagline {
    margin-top: 20px;
    display: flex;
    align-items: center;
    gap: 12px;
    font-size: 22px;
    letter-spacing: 3px;
  }
  .front-mark__square {
    width: 18px;
    height: 18px;
    background: var(--brand-blue);
  }

  /* Back side */
  .back-pattern {
    position: absolute;
    inset: 0;
    background:
      repeating-linear-gradient(-28deg, var(--card-back) 0 34px, var(--pattern-tone) 34px 68px);
    opacity: 0.7;
  }
  .back-mark {
    position: absolute;
    left: 0;
    right: 0;
    top: 395px;
    text-align: center;
    font-weight: 600;
    color: var(--brand-blue);
    text-transform: uppercase;
  }
  .back-mark__name {
    font-size: 50px;
    line-height: 1;
    letter-spacing: 1px;
  }
  .back-mark__tagline {
    margin-top: 8px;
    font-size: 15px;
    letter-spacing: 2.5px;
  }
</style>
</head>
<body>
<main class="canvas">
  <section class="card card--front" aria-label="Card front">
    <div class="contact">
      <h1 class="contact__name">Marcus Hale</h1>
      <ul class="contact__lines">
        <li>044-555 018 273</li>
        <li>info@bayfieldclaims.com</li>
        <li>www.<span class="contact__highlight">bayfieldclaims</span>.com</li>
      </ul>
    </div>
    <div class="front-mark">
      <p class="front-mark__name">Bay<br>field</p>
      <p class="front-mark__tagline"><span class="front-mark__square"></span>Insurance Adjusters</p>
    </div>
  </section>

  <section class="card card--back" aria-label="Card back">
    <div class="back-pattern" role="img" aria-label="Faint tiled background pattern"></div>
    <div class="back-mark">
      <p class="back-mark__name">Bayfield</p>
      <p class="back-mark__tagline">Insurance Adjusters</p>
    </div>
  </section>
</main>
</body>
</html>
```